Burlesque single party (digital) flyer

For promoting an event (burlesque party for singles) we would need a few graphics:
- 1920 x 1080 Version
- 1200 x 628 version
- A6 version
- print-friendly at 300dpi in layered source psd format
- The visual must emphasize the burlesque theme.

The party also includes our lock and key concept for singles to easily meet other singles: Women get a lock, men recieve a key. They can go in the crowd to find a lock the can open to win something: it's just a way to get people to talk to strangers.

Target Market(s)

singles

Industry/Entity Type

Digital

Requirements
Must have
• It should mention both enclosed logo's.
• It should mention:
• - location: De Zonnehal
• - location Address: Marmerlaan 47, 9170 Oostveld-Kanegem
• - Date: 19 mei
• - Tickets in presale only at lumoranight.be
• - Title: Singles GlowNight
• - Title: Burlesque edition
Nice to have
• please visit lumoranight.be to view our actual colors and style
Should not have
• Too nude/erotic. It has to be a stylish, premium and tasteful visual for promoting a burlesque party

```html
<!DOCTYPE html>
<html lang="nl">
<head>
<meta charset="utf-8">
<title>Singles GlowNight – Burlesque Edition</title>
<link href="https://fonts.googleapis.com/css2?family=Audiowide&family=Michroma&display=swap" rel="stylesheet">
<style>
  :root {
    --backdrop: #121018;
    --poster-top: #0b0c1c;
    --poster-bottom: #1c0f26;
    --neon-blue: #3b3bff;
    --neon-core: #e6e8ff;
    --text-light: #f1f1f6;
    --art-mid: #19142c;
    --art-edge: #0e0c1a;
    --accent-red: #d8323c;
    --accent-purple: #a64bd6;
    --tagline: #b9b3d8;
  }
  * { margin: 0; padding: 0; box-sizing: border-box; }
  html, body {
    width: 1200px; height: 1200px; overflow: hidden;
    background: var(--backdrop);
  }
  .poster {
    position: absolute;
    left: 285px; top: 30px;
    width: 630px; height: 1140px;
    border-radius: 28px;
    background: linear-gradient(180deg, var(--poster-top) 0%, #120f28 45%, var(--poster-bottom) 100%);
    overflow: hidden;
    color: var(--text-light);
    font-family: "Michroma", sans-serif;
  }
  .presale {
    position: absolute; top: 78px; left: 0; width: 100%;
    text-align: center;
    font-size: 14px; letter-spacing: 1px;
    text-transform: uppercase;
    white-space: nowrap;
  }
  .heart-art {
    position: absolute; left: 85px; top: 330px;
    width: 460px; height: 470px;
    border-radius: 40px;
    background: radial-gradient(ellipse at 50% 45%, var(--art-mid) 0%, var(--art-edge) 70%, transparent 100%);
  }
  .title-block {
    position: absolute; top: 505px; left: 0; width: 100%;
    text-align: center;
    font-family: "Audiowide", sans-serif;
    text-transform: uppercase;
  }
  .title-frame {
    display: inline-block;
    width: 560px;
    padding: 16px 0 14px;
    border: 3px solid var(--neon-core);
    box-shadow: 0 0 6px var(--neon-blue), 0 0 18px var(--neon-blue), inset 0 0 10px var(--neon-blue);
    font-size: 32px; letter-spacing: 2px;
    color: var(--neon-core);
    text-shadow: 0 0 4px var(--neon-blue), 0 0 12px var(--neon-blue), 0 0 22px var(--neon-blue);
    white-space: nowrap;
  }
  .subtitle {
    margin-top: 22px;
    font-size: 27px; letter-spacing: 1.5px;
    color: var(--neon-core);
    text-shadow: 0 0 4px var(--neon-blue), 0 0 12px var(--neon-blue);
    white-space: nowrap;
  }
  .partners {
    position: absolute; left: 36px; bottom: 72px;
    width: 200px;
  }
  .partner {
    display: flex; align-items: center; gap: 8px;
    margin-top: 16px;
  }
  .partner-mark { width: 22px; height: 22px; flex: none; }
  .partner-mark.square { background: var(--accent-red); }
  .partner-mark.circle { border-radius: 50%; background: var(--accent-purple); }
  .partner-name { font-size: 12px; color: var(--text-light); white-space: nowrap; }
  .partner-tagline { font-size: 7px; color: var(--tagline); margin-top: 3px; white-space: nowrap; }
  .event-info {
    position: absolute; right: 30px; bottom: 62px;
    width: 360px;
    text-align: center;
    font-size: 16px; line-height: 1.6; letter-spacing: 1px;
    text-transform: uppercase;
  }
  .event-line { display: block; white-space: nowrap; }
</style>
</head>
<body>
  <main class="poster">
    <p class="presale">Tickets in presale only at lumoranight.be</p>

    <div class="heart-art" role="img" aria-label="Faceted dark crystal heart illustration"></div>

    <div class="title-block">
      <div class="title-frame">Singles GlowNight</div>
      <div class="subtitle">Burlesque Edition</div>
    </div>

    <div class="partners">
      <div class="partner">
        <span class="partner-mark square"></span>
        <div>
          <div class="partner-name">Solo Kring</div>
          <div class="partner-tagline">Activiteiten &amp; Events voor singles</div>
        </div>
      </div>
      <div class="partner">
        <span class="partner-mark circle"></span>
        <div>
          <div class="partner-name">LumoraNight</div>
          <div class="partner-tagline">brengt mensen samen</div>
        </div>
      </div>
    </div>

    <div class="event-info">
      <span class="event-line">19 mei 2018</span>
      <span class="event-line">De Zonnehal</span>
      <span class="event-line">Marmerlaan 47,</span>
      <span class="event-line">9170 Oostveld-Kanegem</span>
    </div>
  </main>
</body>
</html>
```